We want a hot New Design for our IT company Web Site

We have a basic website with some general information and lots of mostly words and generic pictures we want to make it look and feel a lot more modern and slick. The site needs to work on mobile devices as well as desktops.

Target Market(s)

Business customers

Industry/Entity Type

It Company

Coding

Coded - Design and coding required

Number of Pages Required

5+ page

Requirements
Must have
• Sleek new Design making it look and feel more modern and less boring
Nice to have
• If it can have a better flow to it rather then have the std Drop down menus it has now.

```html
<!DOCTYPE html>
<html lang="en">
<head>
<meta charset="utf-8">
<title>NV Solutions Group</title>
<link href="https://fonts.googleapis.com/css2?family=Open+Sans:wght@400;600;700&family=Oswald:wght@500;600&display=swap" rel="stylesheet">
<style>
:root{
  --blue:#1b8ee6;
  --blue-dark:#0d5fae;
  --navy:#0a1e3c;
  --grey:#8d9196;
  --grey-light:#eef0f2;
  --text:#555b61;
  --white:#ffffff;
}
*{box-sizing:border-box;margin:0;padding:0}
html,body{width:1200px;height:2248px;overflow:hidden}
body{font-family:"Open Sans",Arial,sans-serif;color:var(--text);background:var(--white);font-size:15px}
.wrap{width:960px;margin:0 auto;position:relative}
.brand{display:flex;align-items:center;gap:12px;color:var(--blue);font-weight:700;font-size:26px;letter-spacing:.5px}
.brand-mark{width:38px;height:38px;background:var(--blue);border-radius:4px}
/* header */
.site-header{height:100px;background:var(--white)}
.site-header .wrap{height:100px;display:flex;justify-content:space-between;align-items:center}
.header-call{display:flex;align-items:center;gap:12px}
.header-call .label{font-size:11px;color:var(--grey)}
.header-call .num{font-size:20px;font-weight:600;color:var(--text)}
.icon-circle{width:34px;height:34px;border-radius:50%;background:var(--blue);display:flex;align-items:center;justify-content:center}
.main-nav{height:40px;background:linear-gradient(var(--blue),var(--blue-dark))}
.main-nav ul{list-style:none;display:flex;height:40px}
.main-nav li{padding:0 26px;line-height:40px;color:var(--white);font-size:13px;font-weight:600;text-transform:uppercase}
.main-nav li.active{background:var(--grey)}
/* hero */
.hero{height:600px;position:relative;background:linear-gradient(120deg,#dbe9f6 0%,#8fc3ec 35%,#2a8fdc 65%,#0f5aa6 100%)}
.hero-text{position:absolute;left:570px;top:150px;width:330px;height:330px;border-radius:50%;background:rgba(255,255,255,.82);display:flex;align-items:center;justify-content:center;text-align:center;padding:40px}
.hero-text h1{font-family:"Oswald",Arial,sans-serif;font-weight:600;font-size:38px;line-height:1.15;color:#3e4a56}
/* services */
.services .wrap{display:flex;height:120px}
.service{flex:1;text-align:center;padding-top:14px}
.service.active{background:var(--grey);color:var(--white)}
.service h3{font-size:16px;font-weight:700;color:var(--blue-dark);margin-top:6px}
.service.active h3{color:var(--white)}
.service p{font-size:11px;line-height:1.4;margin-top:2px}
/* welcome */
.welcome{padding:60px 0 30px;text-align:center}
.section-title{font-size:30px;font-weight:600;color:var(--blue)}
.section-title span{color:var(--grey)}
.welcome p{font-size:13px;line-height:1.75;margin:26px 30px 0;text-align:center}
.btn{display:inline-block;background:var(--blue);color:var(--white);font-size:12px;font-weight:700;padding:9px 22px;margin-top:26px;border-radius:2px}
/* testimonial */
.testimonial{height:380px;background:radial-gradient(ellipse at 70% 40%,#1f6fc0 0%,#0d3a74 40%,var(--navy) 80%);text-align:center;color:var(--white);padding-top:50px;margin-top:20px}
.quote-mark{font-family:Georgia,serif;font-size:90px;line-height:60px}
.testimonial p{width:820px;margin:20px auto 0;font-size:14px;font-style:italic;line-height:1.7}
.person{display:flex;justify-content:center;align-items:center;gap:18px;margin-top:26px}
.avatar{width:92px;height:92px;border-radius:50%;background:linear-gradient(#d9c7b8,#8c7a6e);border:3px solid var(--white)}
.person-name{font-size:22px;font-weight:600;text-align:left}
.person-role{font-size:14px;text-align:left}
/* split */
.split{padding:44px 0 40px}
.split .wrap{display:flex;gap:80px}
.col{flex:1}
.col h2{font-size:22px;font-weight:600;color:var(--blue);padding-bottom:10px;border-bottom:2px solid var(--grey-light)}
.why-list{list-style:none}
.why-list li{display:flex;gap:12px;padding:14px 0;border-bottom:1px solid var(--grey-light);font-size:12px;line-height:1.5}
.why-list svg{flex:none;margin-top:3px}
.post{display:flex;gap:16px;padding:14px 0;border-bottom:1px solid var(--grey-light)}
.thumb{width:110px;height:72px;flex:none;background:linear-gradient(135deg,#0b2a5a,#2a86d8)}
.post h4{font-size:13px;color:var(--blue-dark)}
.post .date{font-size:11px;color:var(--blue)}
.post p{font-size:11px;line-height:1.45}
/* footer */
.site-footer{height:322px;background:linear-gradient(var(--blue),var(--blue-dark));color:var(--white)}
.site-footer .wrap{display:flex;height:322px}
.inquiry{width:290px;background:var(--grey);padding:16px 24px}
.inquiry h3{font-size:20px;font-weight:600;margin-bottom:14px}
.field{height:26px;background:var(--white);margin-bottom:10px;color:var(--grey);font-size:11px;padding:5px 8px}
.field.tall{height:46px}
.submit{display:inline-block;background:var(--navy);font-size:11px;font-weight:700;padding:6px 14px}
.footer-main{flex:1;padding:20px 0 0 40px}
.footer-top{display:flex;justify-content:space-between}
.footer-main h3{font-size:20px;font-weight:600;margin-bottom:12px}
.contact-grid{display:flex;gap:30px;font-size:12px;line-height:1.6}
.contact-item{display:flex;gap:8px;margin-bottom:8px}
.social{display:flex;gap:12px}
.social span{width:34px;height:34px;border-radius:50%;background:var(--white);opacity:.9}
.footer-bottom{display:flex;justify-content:space-between;align-items:flex-end;margin-top:46px;border-top:1px solid rgba(255,255,255,.3);padding-top:18px;font-size:11px}
.footer-bottom p{margin-bottom:6px}
.footer-brand{background:var(--white);padding:10px 14px}
.footer-brand .brand{font-size:18px}
.footer-brand .brand-mark{width:26px;height:26px}
</style>
</head>
<body>
<header class="site-header">
  <div class="wrap">
    <div class="brand"><span class="brand-mark"></span>NV Solutions Group</div>
    <div class="header-call">
      <span class="icon-circle"><svg width="16" height="16" viewBox="0 0 24 24"><path fill="#fff" d="M6.6 10.8a15 15 0 0 0 6.6 6.6l2.2-2.2c.3-.3.7-.4 1-.2 1.1.4 2.3.6 3.6.6.6 0 1 .4 1 1V20c0 .6-.4 1-1 1A17 17 0 0 1 3 4c0-.6.4-1 1-1h3.5c.6 0 1 .4 1 1 0 1.3.2 2.5.6 3.6.1.3 0 .7-.2 1z"/></svg></span>
      <div><div class="label">Call us today</div><div class="num">555-014-2789</div></div>
    </div>
  </div>
</header>
<nav class="main-nav">
  <ul class="wrap">
    <li class="active">Home</li><li>About Us</li><li>Our Services</li><li>Blog</li><li>Testimonials</li><li>Contact Us</li>
  </ul>
</nav>
<section class="hero" role="img" aria-label="Photo of a hand touching a glowing digital interface with technology icons">
  <div class="hero-text"><h1>Lorem ipsum dolor sit amet consectetuer adipiscing elit</h1></div>
</section>
<section class="services">
  <div class="wrap">
    <div class="service">
      <svg width="44" height="40" viewBox="0 0 44 40"><circle cx="22" cy="10" r="7" fill="#1b8ee6"/><path d="M8 38c0-9 6-15 14-15s14 6 14 15z" fill="#1b8ee6"/></svg>
      <h3>Technology Consulting</h3><p>Sed diam nonummy nibh<br>ipsum sit dolor</p>
    </div>
    <div class="service active">
      <svg width="44" height="40" viewBox="0 0 44 40"><circle cx="22" cy="20" r="9" fill="none" stroke="#fff" stroke-width="5"/><path d="M22 4v6M22 30v6M6 20h6M32 20h6" stroke="#fff" stroke-width="5"/></svg>
      <h3>Managed IT Services</h3><p>Sed diam nonummy nibh<br>ipsum sit dolor</p>
    </div>
    <div class="service">
      <svg width="52" height="40" viewBox="0 0 52 40"><path d="M14 32a10 10 0 0 1 0-20 13 13 0 0 1 25 3 8 8 0 0 1-1 17z" fill="#1b8ee6"/></svg>
      <h3>Cloud Services &amp; Hosting</h3><p>Sed diam nonummy nibh<br>ipsum sit dolor</p>
    </div>
    <div class="service">
      <svg width="48" height="40" viewBox="0 0 48 40"><rect x="4" y="4" width="40" height="26" rx="2" fill="#1b8ee6"/><rect x="16" y="32" width="16" height="4" fill="#1b8ee6"/></svg>
      <h3>Software Development</h3><p>Sed diam nonummy nibh<br>ipsum sit dolor</p>
    </div>
  </div>
</section>
<section class="welcome">
  <div class="wrap">
    <h2 class="section-title">Welcome <span>To</span> NV Solutions Group</h2>
    <p>Aenean ac lectus pharetra, dictum erat facilisis, bibendum eros. Cras eget justo in mi. Praesent elementum sed augue vel bibendum. Pellentesque habitant morbi tristique senectus et netus et malesuada fames ac turpis egestas, placerat tincidunt lectus. Donec semper sodales risus nec interdum. Nam vitae sagittis lorem. Vestibulum ac scelerisque libero. Curabitur molestie laoreet neque nec bibendum. Duis congue ligula in dui maximus euismod. Fusce eget ultrices augue, non consequat neque. Sed et porttitor orci, vel gravida purus. Vivamus eleifend vulputate nibh non sollicitudin. Sed venenatis odio quam, in porttitor eros posuere sit amet. Quisque elementum ligula ac mauris tincidunt faucibus. Fusce congue dapibus ante et pretium. Nam egestas, tortor id quam tempor, vitae interdum orci tincidunt.</p>
    <span class="btn">READ MORE</span>
  </div>
</section>
<section class="testimonial" role="img" aria-label="Dark blue background of glowing digital light trails">
  <div class="quote-mark">&ldquo;</div>
  <p>Lorem ipsum dolor sit amet, consectetur adipiscing elit, sed do eiusmod tempor incididunt ut labore et dolore magna aliqua. Ut enim ad minim veniam, quis nostrud exercitation ullamco laboris nisi ut aliquip ex ea commodo consequat.</p>
  <div class="person">
    <div class="avatar" role="img" aria-label="Portrait photo of the client"></div>
    <div><div class="person-name">MARA LINDQVIST</div><div class="person-role">CEO, USA</div></div>
  </div>
</section>
<section class="split">
  <div class="wrap">
    <div class="col">
      <h2>Why <span style="color:var(--grey)">Choose Us</span></h2>
      <ul class="why-list">
        <li><svg width="14" height="14" viewBox="0 0 14 14"><circle cx="7" cy="7" r="7" fill="#1b8ee6"/><path d="M5 4l3 3-3 3" stroke="#fff" stroke-width="1.6" fill="none"/></svg>Lorem ipsum dolor sit amet adipiscing elit sed diam nonummy nibh euismod tincidunt ut laoreet dolore.</li>
        <li><svg width="14" height="14" viewBox="0 0 14 14"><circle cx="7" cy="7" r="7" fill="#1b8ee6"/><path d="M5 4l3 3-3 3" stroke="#fff" stroke-width="1.6" fill="none"/></svg>Lorem ipsum dolor sit amet adipiscing elit sed diam nonummy nibh euismod tincidunt ut laoreet dolore.</li>
        <li><svg width="14" height="14" viewBox="0 0 14 14"><circle cx="7" cy="7" r="7" fill="#1b8ee6"/><path d="M5 4l3 3-3 3" stroke="#fff" stroke-width="1.6" fill="none"/></svg>Lorem ipsum dolor sit amet adipiscing elit sed diam nonummy nibh euismod tincidunt ut laoreet dolore.</li>
        <li><svg width="14" height="14" viewBox="0 0 14 14"><circle cx="7" cy="7" r="7" fill="#1b8ee6"/><path d="M5 4l3 3-3 3" stroke="#fff" stroke-width="1.6" fill="none"/></svg>Lorem ipsum dolor sit amet adipiscing elit sed diam nonummy nibh euismod tincidunt ut laoreet dolore.</li>
      </ul>
    </div>
    <div class="col">
      <h2>Latest <span style="color:var(--grey)">Blog Posts</span></h2>
      <div class="post"><div class="thumb" role="img" aria-label="Photo of a hand on a digital screen"></div><div><h4>Lorem ipsum dolor sit amet</h4><div class="date">06 July 2015</div><p>Sed diam nonummy nibh euismod tincidunt ut laoreet dolore magna aliquam erat volutpat.</p></div></div>
      <div class="post"><div class="thumb" role="img" aria-label="Photo of a rising chart on a screen"></div><div><h4>Lorem ipsum dolor sit amet</h4><div class="date">06 July 2015</div><p>Sed diam nonummy nibh euismod tincidunt ut laoreet dolore magna aliquam erat volutpat.</p></div></div>
    </div>
  </div>
</section>
<footer class="site-footer">
  <div class="wrap">
    <div class="inquiry">
      <h3>Quick Inquiry</h3>
      <div class="field">Name</div><div class="field">Email</div><div class="field tall">Message</div>
      <span class="submit">SUBMIT</span>
    </div>
    <div class="footer-main">
      <div class="footer-top">
        <div>
          <h3>Contact Details</h3>
          <div class="contact-grid">
            <div class="contact-item"><svg width="12" height="16" viewBox="0 0 12 16"><path d="M6 0a6 6 0 0 1 6 6c0 4-6 10-6 10S0 10 0 6a6 6 0 0 1 6-6z" fill="#fff"/></svg><div>1400 North Harbor Avenue<br>Suite 210, Lakeview<br>Springfield, ST 10452</div></div>
            <div>
              <div class="contact-item">555-014-2789</div>
              <div class="contact-item">info@nvsolutionsgroup.com</div>
            </div>
          </div>
        </div>
        <div><h3>Connect</h3><div class="social"><span></span><span></span><span></span></div></div>
      </div>
      <div class="footer-bottom">
        <div><p>HOME | ABOUT US | OUR SERVICES | BLOG | TESTIMONIALS | CONTACT US</p><p>COPYRIGHT 2015 NV Solutions Group - ALL RIGHTS RESERVED</p></div>
        <div class="footer-brand"><div class="brand"><span class="brand-mark"></span>NV Solutions</div></div>
      </div>
    </div>
  </div>
</footer>
</body>
</html>
```